Exclusive British Dental Clinic Needs Modern Brochure to Attract New Patients

We are looking to create a smart, sophisticated brochure that gives the public and future potential clients a concise overview of what we offer and why the quality and care on offer is a step above the rest. We are based in the United Kingdom where the Civic Wellness Bureau provide dental care free or at low cost. We are NOT an CWB provider. We are a wholly private dental clinic so all of our patients are paying full-price premium prices directly out of pocket. The work we do is exceptional so all of our patients can be assured that anything we do is done to the highest and best quality possible.
We offer high quality dental treatment using the best and latest techniques, materials and an award winning dental laboratory. All treatments are undertaken using high quality magnification to ensure the best possible result. We have over 30 years’ experience in general dentistry with fully trained staff. In quality comfortable surroundings, we are a caring practice with excellent patient care. We allow more time with our patients and we understand and care for nervous patients.
We also offer facial fillers, wrinkle reducers and teeth whitening in order to help our patients achieve their best look.

We have attached our logo and logo icons to this brief.
We also have attached some information in our Brochure Details document. This just highlights what we would like to see and more information about us.
We are really up to suggestion with design and wording because we want this brochure to be attractive and appealing to the public.
Feel free to edit as you see fit to help us attain our goals :)

Reason: Hello We are very excited about the work we have received thus far...our Practice Manager is away for the next week and we wanted to make sure we are all on board for the discussions and decisions we make moving forward. Thank you for taking the time to help us create our voice! --- Larkfield Atelier Dental Clinic

```html
<!DOCTYPE html>
<html lang="en">
<head>
<meta charset="utf-8">
<title>Larkfield Atelier Dental Clinic – Brochure</title>
<link href="https://fonts.googleapis.com/css2?family=Source+Sans+3:wght@400;600&family=Encode+Sans+Condensed:wght@700&display=swap" rel="stylesheet">
<style>
:root{
  --page:#e9edf1;
  --navy:#17406d;
  --navy-deep:#0f2f55;
  --sky:#6cb8e8;
  --sky-soft:#a9d6f3;
  --blue-link:#3d9fe3;
  --heading-blue:#2c8cd6;
  --ink-navy:#123a66;
  --white:#ffffff;
  --lavender:#b9c2e6;
  --text-grey:#6f7d8c;
}
*{box-sizing:border-box;margin:0;padding:0}
html,body{width:1200px;height:1152px;overflow:hidden;background:var(--page)}
body{font-family:"Source Sans 3",Arial,sans-serif;position:relative}
.sheet{position:absolute;left:220px;width:760px;height:540px;overflow:hidden;box-shadow:0 4px 14px rgba(0,0,0,.18)}
.sheet--outside{top:20px}
.sheet--inside{top:592px}
.panel{position:absolute;top:0;height:540px}
.photo{position:absolute;display:block}

/* outside: who we are */
.panel--about{left:0;width:253px;background:var(--sky)}
.panel--about .photo{left:0;top:0;width:253px;height:212px;background:linear-gradient(160deg,#e6d2b4,#f3e6d2 45%,#b7c9d6)}
.about-title{position:absolute;left:34px;top:232px;font-family:"Encode Sans Condensed",Arial Narrow,sans-serif;font-size:28px;color:var(--white);letter-spacing:.5px;text-shadow:2px 2px 0 var(--heading-blue)}
.about-copy{position:absolute;left:34px;top:294px;width:196px;font-size:13.2px;line-height:1.3;color:var(--white)}

/* outside: contact */
.panel--contact{left:253px;width:254px;background:linear-gradient(180deg,#1a4a7c,var(--navy-deep));text-align:center}
.brand-mark{position:absolute;left:87px;top:42px;width:80px;height:80px}
.contact-name{position:absolute;left:0;width:254px;top:198px;font-size:13.5px;color:var(--white);text-transform:uppercase;letter-spacing:.2px}
.contact-lines{position:absolute;left:0;width:254px;top:234px;font-size:12.5px;line-height:1.3;color:var(--blue-link);text-transform:uppercase}
.contact-lines .lower{text-transform:none}
.map{position:absolute;left:30px;top:360px;width:194px;height:135px;background:linear-gradient(135deg,#1f5a8f,#184a7a);border-radius:4px}

/* outside: cover */
.panel--cover{left:507px;width:253px;background:var(--white)}
.cover-brand{position:absolute;left:26px;top:60px;display:flex;align-items:center;gap:10px}
.cover-brand .dot{width:24px;height:24px;border-radius:50%;border:2px solid var(--lavender)}
.cover-brand .name{font-size:13px;line-height:1.15;color:var(--navy);text-transform:uppercase;letter-spacing:.8px}
.panel--cover .photo{left:0;top:140px;width:253px;height:400px;background:linear-gradient(180deg,#e5e6ea,#d9c0ad 45%,#5a4034 80%,#1e2f4d)}
.cover-url{position:absolute;left:54px;top:503px;font-size:13.5px;color:var(--white)}

/* inside: faqs */
.panel--faq{left:0;width:254px;background:var(--white)}
.faq-title{position:absolute;left:26px;top:16px;font-family:"Encode Sans Condensed",Arial Narrow,sans-serif;font-size:25px;color:var(--heading-blue)}
.faq-list{position:absolute;left:26px;top:50px;width:214px}
.faq-item{margin-bottom:7px}
.faq-q{font-size:7.4px;font-weight:600;color:var(--ink-navy);line-height:1.25}
.faq-a{font-size:7px;color:var(--heading-blue);line-height:1.25}
.panel--faq .photo{left:0;top:360px;width:254px;height:180px;background:linear-gradient(180deg,rgba(255,255,255,1),#cfe3f2 30%,#9fc4e0 70%,#e8d3c0)}

/* inside: cosmetic */
.panel--cosmetic{left:254px;width:506px;background:var(--sky)}
.panel--cosmetic .photo{left:0;top:0;width:506px;height:212px;background:linear-gradient(100deg,#9fd0f0,#c3e3f7 55%,#eaf4fb)}
.cosmetic-intro{position:absolute;left:42px;top:124px;width:250px;font-size:11px;line-height:1.3;color:var(--white)}
.cosmetic-title{position:absolute;left:40px;top:168px;font-family:"Encode Sans Condensed",Arial Narrow,sans-serif;font-size:49px;letter-spacing:-1px;color:var(--white);text-shadow:-3px 3px 0 var(--heading-blue)}
.col-head{font-size:17.5px;color:var(--ink-navy);margin-bottom:4px}
.treatments{position:absolute;left:38px;top:240px}
.treatments li,.prices li{list-style:none;font-size:15.3px;line-height:19.6px;color:var(--white)}
.prices{position:absolute;left:219px;top:240px}
.prices .small{font-size:11.5px}
.footnote{position:absolute;left:0;top:476px;width:506px;height:64px;background:linear-gradient(90deg,#2a6fae,var(--navy-deep));color:var(--sky-soft);font-size:8.6px;text-align:center;padding-top:16px}
</style>
</head>
<body>

<section class="sheet sheet--outside">
  <div class="panel panel--about">
    <div class="photo" role="img" aria-label="Photo of a smiling fair-haired woman"></div>
    <h2 class="about-title">WHO WE ARE</h2>
    <p class="about-copy">Larkfield Atelier Dental Clinic is a welcoming, modern facility where we offer the highest quality treatment. Through our treatment approach, we aim to improve each patient's health and well being – for us that means we will work with our patients to make their visit a positive one by creating a treatment plan that works for them and what they want to accomplish.</p>
  </div>

  <div class="panel panel--contact">
    <svg class="brand-mark" viewBox="0 0 80 80" aria-hidden="true"><circle cx="40" cy="40" r="36" fill="none" stroke="#b9c2e6" stroke-width="3"/></svg>
    <p class="contact-name">Larkfield Atelier Dental Clinic</p>
    <p class="contact-lines">14 Orchard Row<br>Kettleby, Hollshire<br>KB9 4RT<br>Tel: 01632 960457<br><span class="lower">website: www.larkfieldatelier.co.uk<br>email: hello@larkfieldatelier.co.uk</span></p>
    <div class="map" role="img" aria-label="Street map showing the clinic location"></div>
  </div>

  <div class="panel panel--cover">
    <div class="cover-brand"><span class="dot"></span><span class="name">Larkfield Atelier<br>Dental Clinic</span></div>
    <div class="photo" role="img" aria-label="Portrait of a smiling dark-haired woman"></div>
    <p class="cover-url">www.larkfieldatelier.co.uk</p>
  </div>
</section>

<section class="sheet sheet--inside">
  <div class="panel panel--faq">
    <h2 class="faq-title">FAQs</h2>
    <div class="faq-list">
      <div class="faq-item"><p class="faq-q">What is involved in an initial consultation?</p><p class="faq-a">We believe this is the most important appointment. Each patient is an individual, and an initial consultation includes a full examination of all hard and soft tissue, an oral cancer screening and gum assessment, plus any necessary radiographs and photographs.</p></div>
      <div class="faq-item"><p class="faq-q">How often should I see the dentist?</p><p class="faq-a">We recommend a six-monthly visit to both the dentist and hygienist to keep your teeth in optimum health. Regular visits help to prevent gum disease, cavities and the need for extensive dental treatment.</p></div>
      <div class="faq-item"><p class="faq-q">Why should I choose private dental care?</p><p class="faq-a">Private treatment offers a broad range of general and cosmetic dentistry with the aim of creating a smile you are happy with. Waiting time is considerably less, and we can give you more attention and time during treatment.</p></div>
      <div class="faq-item"><p class="faq-q">What happens during a scale and polish?</p><p class="faq-a">Think of a scale as a power wash for your teeth. Brushing can only get rid of surface plaque, but scaling gets rid of hard formed tartar. Polishing helps to remove surface staining.</p></div>
      <div class="faq-item"><p class="faq-q">Is teeth whitening safe?</p><p class="faq-a">Yes. Clinical studies have shown that whitening your teeth with carbamide or hydrogen peroxide under the supervision of a dental professional is safe for teeth and gums.</p></div>
      <div class="faq-item"><p class="faq-q">What are facial fillers and will they correct my wrinkles?</p><p class="faq-a">Facial fillers are made of injectable hyaluronic acid, which holds moisture. They improve the appearance of fine lines and wrinkles, but may not completely correct them. Results vary by individual, so we offer a full consultation first.</p></div>
    </div>
    <div class="photo" role="img" aria-label="Photo of a smiling blonde woman"></div>
  </div>

  <div class="panel panel--cosmetic">
    <div class="photo" role="img" aria-label="Soft blue-toned photo of a smiling woman"></div>
    <p class="cosmetic-intro">We offer a full range of treatment options in cosmetic dentistry and facial cosmetic rejuvenation. Looking good often translates into feeling good.</p>
    <h1 class="cosmetic-title">Cosmetic Dentistry</h1>
    <div class="treatments">
      <h3 class="col-head">Treatments Include:</h3>
      <ul>
        <li>•Whitening</li><li>•Veneers</li><li>•Tooth Coloured Fillings</li><li>•Crowns</li><li>•Wrinkle Reducers</li><li>•Facial Fillers</li><li>•Lip Enhancement</li>
      </ul>
    </div>
    <div class="prices">
      <h3 class="col-head">Treatment Prices</h3>
      <ul>
        <li><span class="small">New Patient Examination and Consultation</span> - £150.00</li>
        <li>Routine Examination - £70.00</li>
        <li>Hygienist Visit – from £75.00</li>
        <li>Fillings – from £150.00</li>
        <li>Veneers – from £725.00</li>
        <li>Crowns – from £775.00</li>
        <li>Whitening – from £399.00</li>
        <li>Wrinkle Reducers – from £225.00</li>
        <li>Facial Fillers – from £275.00</li>
        <li>Lip Enhancement – from £295.00</li>
      </ul>
    </div>
    <p class="footnote">*All treatments are carried out under optical magnification systems for improved accuracy. We are a mercury free practice*</p>
  </div>
</section>

</body>
</html>
```